Brightvale senior care need flyer design

Flyer design to introduce physician working with brightvale senior care.
the flyer can be simple but need to be catchy.
A sample attached just mainly for reference purpose.
The format must be editable with ms word.

thank you

```html
<!DOCTYPE html>
<html lang="en">
<head>
<meta charset="utf-8">
<title>Brightvale Senior Care – Introducing Dr. Wen</title>
<link href="https://fonts.googleapis.com/css2?family=Source+Sans+3:wght@300;400;600;700;900&display=swap" rel="stylesheet">
<style>
  :root {
    --red: #d71f26;
    --navy: #1f2a78;
    --navy-deep: #0f2144;
    --header-blue: #1d3f6e;
    --ink: #1a1a1a;
    --white: #ffffff;
  }
  html, body { margin: 0; padding: 0; overflow: hidden; background: var(--white); }
  .flyer {
    position: relative;
    width: 851px; height: 1200px;
    box-sizing: border-box;
    border: 5px solid var(--red);
    background: var(--white);
    font-family: "Source Sans 3", Arial, sans-serif;
    color: var(--ink);
    overflow: hidden;
  }
  .abs { position: absolute; }

  .hero {
    left: 32px; top: 35px; width: 775px; height: 228px;
    background: linear-gradient(100deg, var(--navy-deep) 0%, var(--header-blue) 55%, #2b5a8c 100%);
    overflow: hidden;
  }
  .hero-photo {
    position: absolute; right: 0; top: 0; width: 360px; height: 228px;
    background: linear-gradient(90deg, rgba(43,90,140,0) 0%, #6f8fb3 45%, #d9e2ec 80%, #f3f5f8 100%);
  }
  .hero-title {
    position: absolute; left: 38px; top: 76px; margin: 0;
    font-weight: 300; font-size: 56px; letter-spacing: -1px;
    color: var(--white); line-height: 1;
  }

  .intro-band {
    left: 32px; top: 263px; width: 775px; height: 55px;
    background: var(--red); color: var(--white);
    font-weight: 700; font-size: 15.5px; line-height: 21px;
    text-align: center; display: flex; align-items: center; justify-content: center;
    padding: 0 40px; box-sizing: border-box;
  }

  .portrait-frame {
    left: 86px; top: 352px; width: 170px; height: 204px;
    border: 5px solid var(--navy); background: var(--white); box-sizing: border-box;
  }
  .doctor-name {
    left: 292px; top: 338px; margin: 0;
    font-weight: 300; font-size: 72px; line-height: 1; color: var(--red);
  }
  .credentials {
    left: 256px; top: 436px; width: 499px; height: 33px;
    background: var(--navy); color: var(--white);
    font-weight: 700; font-size: 18.5px; line-height: 33px;
    padding-left: 40px; box-sizing: border-box;
  }
  .role {
    left: 296px; top: 488px; margin: 0;
    font-weight: 900; font-size: 32px; line-height: 35px; color: var(--red);
    letter-spacing: 0.2px;
  }

  .body-copy {
    left: 96px; top: 580px; width: 659px;
    font-size: 14px; line-height: 18px;
  }
  .body-copy p { margin: 0 0 4px; text-align: justify; }
  .label { color: var(--red); font-weight: 700; }
  .interests { list-style: none; margin: 10px 0 6px; padding: 0; }
  .interests li { font-weight: 700; font-size: 19px; line-height: 32px; }

  .stethoscope {
    left: 565px; top: 688px; width: 190px; height: 172px;
    background: radial-gradient(ellipse at 55% 55%, #c9cdd2 0%, #e35a5f 30%, rgba(215,31,38,0.25) 58%, rgba(255,255,255,0) 72%);
  }

  .appointment-bar {
    left: 96px; top: 963px; width: 659px; height: 29px;
    background: var(--navy); color: var(--white);
    font-size: 16.5px; line-height: 29px; text-align: center;
  }
  .contact-label {
    left: 0; top: 998px; width: 841px; text-align: center;
    font-weight: 700; font-size: 16.5px; color: var(--red);
  }
  .brand {
    left: 0; top: 1030px; width: 841px;
    display: flex; justify-content: center;
  }
  .brand-row { display: flex; align-items: center; gap: 10px; }
  .brand-dot { width: 30px; height: 30px; border-radius: 50%; background: var(--red); }
  .brand-name { font-weight: 600; font-size: 34px; line-height: 38px; color: var(--navy); }
  .address {
    left: 0; top: 1100px; width: 841px; text-align: center;
    font-weight: 700; font-size: 16px; line-height: 29px;
  }
  .address .gap { display: inline-block; width: 24px; }
</style>
</head>
<body>
<main class="flyer">
  <header class="hero abs">
    <div class="hero-photo" role="img" aria-label="Photograph of a doctor in a white coat with a stethoscope, touching a digital medical icon"></div>
    <h1 class="hero-title">INTRODUCING</h1>
  </header>

  <div class="intro-band abs">Brightvale senior care is formed by a group of geriatricians to provide medical consultation in both community and permanent residential care for patients over 65 years old.</div>

  <div class="portrait-frame abs"></div>
  <h2 class="doctor-name abs">Dr. WEN</h2>
  <div class="credentials abs">MBBS(Eastvale), Fracp, Clin Dip Pall med.</div>
  <h3 class="role abs">CONSULTANT GERIATRICIAN<br>AND PHYSICIAN</h3>

  <section class="body-copy abs">
    <p>We are very pleased to introduce you to Consultant Geriatrician and Physician who has commenced consulting at Kestrel Private Hospital and is available to see patients who are 65 years and over.</p>
    <p>Completed his specialist training with Northfield Health in 2012 and then undertook 6 months of diploma training in palliative care medicine prior to commencing as a consultant geriatrician.</p>
    <p class="label">He has an interest in all geriatric related problems, with special interest in:</p>
    <ol class="interests">
      <li>1. Comperhensive Geriatric Assessment (Over 65 years)</li>
      <li>2. Memory assessment</li>
      <li>3. Fall and balance assessment</li>
      <li>4. Polypharmacy</li>
    </ol>
    <p>He is also available to visit residential care facilities, should you require any advice.</p>
    <p class="label">Other language spoken:</p>
    <p>Mandarian, Cantonese and Malay</p>
    <p class="label">Marcus can be contacted on 0400 555 120 for patient advice.</p>
    <p>Alternatively, you can fax your referral especially for residents in residential care facilities to <span class="label">(03) 5550 0142.</span></p>
  </section>

  <div class="stethoscope abs" role="img" aria-label="Red and silver stethoscope"></div>

  <div class="appointment-bar abs">To arrange and appointment for your patient with Dr. Wen</div>
  <div class="contact-label abs">Please contact:</div>
  <div class="brand abs">
    <div class="brand-row">
      <span class="brand-dot"></span>
      <span class="brand-name">Brightvale Senior Care</span>
    </div>
  </div>
  <div class="address abs">
    Main room,&nbsp; Suite 3.09, Larkin Medical Glenmoor, 42-44 Ashford Street, Glenmoor VIC 3199<br>
    T: (03) 5550 0142<span class="gap"></span>F: (03) 5550 0142
  </div>
</main>
</body>
</html>
```